Harbor Tandem Web Design Project

We need a website design for a start up company called "Harbor Tandem". We provide business consultancy services as well as technology-related services (IT). The design should communicate simplicity and elegance. The domain name of the site will be harbortandem.com. The logo of the company is https://files.pinvault.net/u/8147206/7730_2049185_31947_image.jpg
Updates

Target Market(s)

SMB, Corporates, Semi-governments, Governments.

Industry/Entity Type

Business

Requirements
Must have
• - The background of the pages should be white or soft grey, but we are open for suggestions.
- The pages should have nice menu animations.
- The pages should be "portal-style", with multiple placeholders for different sections and multiple tabs.
Nice to have
• The page should auto-fit the screen and scroll vertically as much as needed.
Should not have
• - Flash Animations.
- Generic Photos.

```html
<!DOCTYPE html>
<html lang="en">
<head>
<meta charset="utf-8">
<title>Harbor Tandem</title>
<link href="https://fonts.googleapis.com/css2?family=Arimo:wght@400;700&display=swap" rel="stylesheet">
<style>
:root{
  --red:#c4161c;
  --red-dark:#8e0c10;
  --blue:#1d6fb8;
  --blue-dark:#0c4f8f;
  --sky:#5aaee0;
  --sky-light:#d6ecf8;
  --nav:#3a3a3a;
  --nav-dark:#262626;
  --ink:#2b2b2b;
  --text:#444;
  --muted:#8a8a8a;
  --panel:#d3e1ea;
  --footer:#2e2e2e;
  --footer-text:#9a9a9a;
}
*{margin:0;padding:0;box-sizing:border-box}
html,body{width:767px;height:1200px;overflow:hidden;background:#fff}
body{font-family:"Arimo",Arial,sans-serif;color:var(--text);position:relative}
.abs{position:absolute}

.header{left:0;top:0;width:767px;height:127px;background:linear-gradient(#e6e6e6,#d2d2d2)}
.search{left:549px;top:14px;width:79px;height:18px;background:#3d3d3d;border:1px solid #222;border-radius:2px;color:#ddd;font-size:10px;padding:3px 6px}
.search svg{position:absolute;right:5px;top:3px}
.login{left:630px;top:14px;width:42px;height:18px;background:var(--red);border:1px solid var(--red-dark);border-radius:2px;color:#fff;font-size:10px;text-align:center;line-height:16px}
.brand{left:112px;top:58px;display:flex;align-items:center;gap:8px}
.brand-dot{width:22px;height:22px;border-radius:50%;background:var(--blue-dark)}
.brand-name{font-size:22px;font-weight:700;color:var(--blue-dark)}
.tagline{left:335px;top:66px;font-size:15px;line-height:19px;color:#555}
.tagline .r{color:var(--red)} .tagline .b{color:var(--blue)}

.nav{left:0;top:127px;width:767px;height:36px;background:linear-gradient(#474747,var(--nav-dark));border-top:1px solid #777}
.nav a{position:absolute;top:0;height:36px;line-height:36px;text-align:center;font-size:9.5px;color:#ddd;text-decoration:none;border-right:1px solid #222}
.nav a.active{background:linear-gradient(#2f8ee0,var(--blue-dark));color:#fff}
.nav a.open{background:#555}
.dropdown{left:454px;top:164px;width:128px;background:rgba(60,60,60,.95)}
.dropdown div{height:18px;line-height:18px;padding-left:10px;font-size:9px;color:#ccc}
.dropdown .on{background:#222;color:#fff}

.hero{left:0;top:163px;width:767px;height:218px;background:linear-gradient(var(--sky-light),var(--sky) 85%)}
.hero-art{left:130px;top:210px;width:225px;height:168px;background:linear-gradient(90deg,#c9a68c,#3a2a24 50%,#e4a32a);border-radius:6px}
.arrow{top:256px}
.hero-title{left:370px;top:212px;width:270px;font-size:14px;line-height:18px;color:#333}
.hero-copy{left:372px;top:253px;width:255px;font-size:8.3px;line-height:10.8px;color:#333}
.learn{left:528px;top:326px;width:91px;height:18px;background:var(--red);border:1px solid var(--red-dark);color:#fff;font-size:10px;font-weight:700;line-height:16px;padding-left:24px}
.learn svg{position:absolute;left:8px;top:4px}
.dots{left:372px;top:356px;display:flex;gap:3px}
.dots span{width:6px;height:6px;border-radius:50%;background:#444}
.dots span.on{background:#fff}

.band{left:0;top:381px;width:767px;height:52px;background:linear-gradient(#cfd5dc,#e2e6ea)}
.quote{left:176px;top:378px;width:284px;height:60px;background:linear-gradient(#c4161c,#9a0d12);border-radius:3px;color:#fff;font-size:12px;line-height:14.4px;text-align:center;padding:9px 14px;box-shadow:0 2px 3px rgba(0,0,0,.3)}
.consult{left:495px;top:395px;width:142px;height:35px;background:linear-gradient(#1f7fd2,var(--blue-dark));border-radius:3px;color:#fff;font-size:15px;font-weight:700;line-height:35px;padding-left:8px}
.consult .chev{position:absolute;right:0;top:0;width:32px;height:35px;border-left:1px solid #5fa6e6}

.sec-title{left:104px;font-size:16.5px;font-weight:700;color:var(--ink)}
.more{left:589px;font-size:11px;color:var(--red);display:flex;align-items:center;gap:6px}
.more i{width:16px;height:14px;background:var(--red);display:flex;align-items:center;justify-content:center}
.rule{left:102px;width:563px;height:1px;background:#bbb}

.col-title{font-size:10.5px;font-weight:700;color:var(--ink);top:513px}
.badge{width:84px;height:84px;border-radius:50%;background:radial-gradient(#fff,#e2e2e2);border:2px solid #ddd;box-shadow:0 1px 3px rgba(0,0,0,.3);text-align:center}
.badge span{position:absolute;left:0;right:0;bottom:12px;font-size:15px;font-weight:700;color:var(--red)}
.col-text{width:168px;font-size:6.9px;line-height:10.9px;color:#555;top:536px}
.read{top:624px;width:70px;height:18px;background:var(--red);border:1px solid var(--red-dark);border-radius:2px;color:#fff;font-size:10px;text-align:center;line-height:16px}

.intro{left:104px;top:721px;width:560px;font-size:8px;line-height:11px;color:#444}
.table{top:761px;width:276px;height:185px;background:var(--panel);box-shadow:0 1px 2px rgba(0,0,0,.2)}
.table-head{height:24px;color:#fff;font-size:15px;text-align:center;line-height:24px}
.table ul{list-style:none;padding:4px 8px}
.table li{border-bottom:1px dotted #aab;font-size:8px;color:#333;text-align:center;padding:4px 0;line-height:10px}
.table li:last-child{border:0}
.table li svg{vertical-align:-2px;margin-right:6px}
.shelf{top:947px;width:252px;height:4px;background:#aaa;border-radius:0 0 4px 4px}

.footer{left:0;top:990px;width:767px;height:170px;background:var(--footer)}
.f-head{top:1005px;font-size:11px;color:#ddd}
.f-list{list-style:none;font-size:8px;color:var(--footer-text)}
.f-list li{height:17px;display:flex;align-items:center;gap:12px}
.f-list .bul{width:4px;height:4px;background:var(--red);border-radius:50%;margin-left:6px}
.f-list .ico{width:9px;height:9px;background:var(--red);border-radius:1px}
.f-blog-t{left:230px;top:1036px;font-size:9px;font-weight:700;color:#aaa}
.f-blog{left:230px;top:1054px;width:130px;font-size:7px;line-height:10.8px;color:#888}
.copy{left:0;top:1170px;width:767px;text-align:center;font-size:8px;color:#555}
</style>
</head>
<body>

<div class="abs header"></div>
<div class="abs search">Search
  <svg width="10" height="10" viewBox="0 0 10 10"><circle cx="4" cy="4" r="3" fill="none" stroke="#ddd" stroke-width="1.4"/><line x1="6.3" y1="6.3" x2="9" y2="9" stroke="#ddd" stroke-width="1.6"/></svg>
</div>
<div class="abs login">Log in</div>
<div class="abs brand"><span class="brand-dot"></span><span class="brand-name">Harbor Tandem</span></div>
<div class="abs tagline">We develop <span class="r">B2B</span> and <span class="b">B2C</span> SAAS based solutions &amp;<br>e-commerce portals for companies</div>

<nav class="abs nav">
  <a class="active" style="left:97px;width:53px">Home</a>
  <a style="left:150px;width:62px">About Us</a>
  <a style="left:212px;width:70px">Case Study</a>
  <a style="left:282px;width:50px">Clients</a>
  <a style="left:332px;width:41px">Blog</a>
  <a style="left:373px;width:41px">B2B</a>
  <a style="left:414px;width:39px">B2C</a>
  <a class="open" style="left:453px;width:77px">Our Services</a>
  <a style="left:530px;width:64px">Marketing</a>
  <a style="left:594px;width:72px;border:0">Contact Us</a>
</nav>

<div class="abs hero"></div>
<div class="abs hero-art" role="img" aria-label="Photo of a woman holding an apple labelled B2B and an orange labelled B2C"></div>
<svg class="abs arrow" style="left:102px" width="20" height="28" viewBox="0 0 20 28"><path d="M16 2 L4 14 L16 26" fill="none" stroke="#c4161c" stroke-width="6"/></svg>
<svg class="abs arrow" style="left:646px" width="20" height="28" viewBox="0 0 20 28"><path d="M4 2 L16 14 L4 26" fill="none" stroke="#c4161c" stroke-width="6"/></svg>
<div class="abs hero-title">How do you market differently to B2B than B2C? Share your best practices here.</div>
<div class="abs hero-copy">Nam liber tempor cum soluta nobis eleifend option congue nihil imperdiet doming id quod mazim placerat facer possim assum. Lorem ipsum dolor sit amet, consectetuer adipiscing elit, sed diam nonummy nibh euismod tincidunt ut laoreet dolore magna aliquam erat volutpat. Ut wisi enim ad minim veniam, quis nostrud exerci tation ullamcorper suscipit lobortis nisl ut aliquip ex ea commodo</div>
<div class="abs learn"><svg width="8" height="9" viewBox="0 0 8 9"><path d="M1 0 L6 4.5 L1 9" fill="none" stroke="#fff" stroke-width="2"/></svg>Learn Now!</div>
<div class="abs dots"><span></span><span class="on"></span><span></span><span></span></div>

<div class="abs dropdown">
  <div>Marketing Consultant</div>
  <div class="on">Business Plan</div>
  <div>Advertise</div>
  <div>Sales</div>
</div>

<div class="abs band"></div>
<div class="abs quote">Nam liber tempor cum soluta nobis eleifend option congue nihil imperdiet doming id quod mazim placerat facer possim assum.</div>
<div class="abs consult">Consult NOW!
  <span class="abs chev"><svg width="32" height="35" viewBox="0 0 32 35"><path d="M11 8 L21 17.5 L11 27" fill="none" stroke="#fff" stroke-width="4"/></svg></span>
</div>

<div class="abs sec-title" style="top:469px">WHAT WE DO?</div>
<div class="abs more" style="top:472px"><i><svg width="7" height="9" viewBox="0 0 7 9"><path d="M1 0 L5.5 4.5 L1 9" fill="none" stroke="#fff" stroke-width="2"/></svg></i>More info</div>
<div class="abs rule" style="top:491px"></div>

<div class="abs col-title" style="left:199px">What is Busines to Busines?</div>
<div class="abs badge" style="left:102px;top:531px"><svg class="abs" style="left:22px;top:12px" width="40" height="28" viewBox="0 0 40 28"><circle cx="12" cy="5" r="5" fill="#c4161c"/><circle cx="28" cy="5" r="5" fill="#c4161c"/><rect x="4" y="11" width="16" height="17" rx="3" fill="#c4161c"/><rect x="20" y="11" width="16" height="17" rx="3" fill="#c4161c"/></svg><span>B2B</span></div>
<div class="abs col-text" style="left:198px">When you are marketing to a B2B you want to focus on the logic of the product. You do this by focusing on the features of the product. There is little to no personal emotion involved in the purchasing decision. You want to focus on understanding the organizational buyers and how they operate within the confines of their organization's procedures.</div>
<div class="abs read" style="left:290px">Read more</div>

<div class="abs col-title" style="left:487px">What is Busines to Cunsumer?</div>
<div class="abs badge" style="left:391px;top:531px"><svg class="abs" style="left:24px;top:12px" width="36" height="30" viewBox="0 0 36 30"><circle cx="10" cy="5" r="4.5" fill="#c4161c"/><circle cx="26" cy="5" r="4.5" fill="#c4161c"/><rect x="3" y="11" width="14" height="19" rx="3" fill="#c4161c"/><rect x="19" y="11" width="14" height="19" rx="3" fill="#c4161c"/></svg><span>B2C</span></div>
<div class="abs col-text" style="left:486px">When you are marketing to a consumer you want to focus on the benefits of the product. Their decision is more emotional. Consumers are different in that they demand a variety of distribution channels for convenience, not so with the B2B market. Consumers are less likely to be interested in a lengthy marketing message.</div>
<div class="abs read" style="left:587px">Read more</div>

<div class="abs sec-title" style="top:687px">WHAT DEFERENCE BETWEEN B2B &amp; B2C?</div>
<div class="abs more" style="top:689px"><i><svg width="7" height="9" viewBox="0 0 7 9"><path d="M1 0 L5.5 4.5 L1 9" fill="none" stroke="#fff" stroke-width="2"/></svg></i>More info</div>
<div class="abs rule" style="top:709px"></div>
<div class="abs intro">There is a difference between marketing to a business and marketing to a consumer, believe it or not. Although you are still selling a product to a person experience shows that the difference between these two types of markets runs deep Let me see if I can explain even further.</div>

<div class="abs table" style="left:102px">
  <div class="table-head" style="background:linear-gradient(#d01a20,#a00e13)">B2B</div>
  <ul>
    <li><svg width="10" height="9" viewBox="0 0 10 9"><path d="M1 5 L4 8 L9 1" fill="none" stroke="#4a9a20" stroke-width="2"/></svg>Group decision making</li>
    <li><svg width="10" height="9" viewBox="0 0 10 9"><path d="M1 5 L4 8 L9 1" fill="none" stroke="#4a9a20" stroke-width="2"/></svg>Multiple possible objections</li>
    <li><svg width="10" height="9" viewBox="0 0 10 9"><path d="M1 5 L4 8 L9 1" fill="none" stroke="#4a9a20" stroke-width="2"/></svg>Influence the person, and they become an advocate internally</li>
    <li><svg width="10" height="9" viewBox="0 0 10 9"><path d="M1 5 L4 8 L9 1" fill="none" stroke="#4a9a20" stroke-width="2"/></svg>Influenced mainly by rational arguments</li>
    <li><svg width="10" height="9" viewBox="0 0 10 9"><path d="M1 5 L4 8 L9 1" fill="none" stroke="#4a9a20" stroke-width="2"/></svg>Investment proposal process</li>
    <li><svg width="10" height="9" viewBox="0 0 10 9"><path d="M1 5 L4 8 L9 1" fill="none" stroke="#4a9a20" stroke-width="2"/></svg>Purchase process is complex and usually requires several meetings, often involving groups of people from both sides</li>
    <li><svg width="10" height="9" viewBox="0 0 10 9"><path d="M1 5 L4 8 L9 1" fill="none" stroke="#4a9a20" stroke-width="2"/></svg>Usually face to face is required</li>
    <li><svg width="10" height="9" viewBox="0 0 10 9"><path d="M1 5 L4 8 L9 1" fill="none" stroke="#4a9a20" stroke-width="2"/></svg>Generally smaller audiences</li>
  </ul>
</div>
<div class="abs shelf" style="left:114px"></div>

<div class="abs table" style="left:389px">
  <div class="table-head" style="background:linear-gradient(#2084d8,var(--blue-dark))">B2C</div>
  <ul>
    <li><svg width="10" height="9" viewBox="0 0 10 9"><path d="M1 5 L4 8 L9 1" fill="none" stroke="#4a9a20" stroke-width="2"/></svg>Single decision-maker</li>
    <li><svg width="10" height="9" viewBox="0 0 10 9"><path d="M1 5 L4 8 L9 1" fill="none" stroke="#4a9a20" stroke-width="2"/></svg>Individual possible objections</li>
    <li><svg width="10" height="9" viewBox="0 0 10 9"><path d="M1 5 L4 8 L9 1" fill="none" stroke="#4a9a20" stroke-width="2"/></svg>Influence the person, close the sale</li>
    <li><svg width="10" height="9" viewBox="0 0 10 9"><path d="M1 5 L4 8 L9 1" fill="none" stroke="#4a9a20" stroke-width="2"/></svg>Influence by emotional arguments</li>
    <li><svg width="10" height="9" viewBox="0 0 10 9"><path d="M1 5 L4 8 L9 1" fill="none" stroke="#4a9a20" stroke-width="2"/></svg>Funds easily available</li>
    <li><svg width="10" height="9" viewBox="0 0 10 9"><path d="M1 5 L4 8 L9 1" fill="none" stroke="#4a9a20" stroke-width="2"/></svg>A single face-to-face contact may lead to purchase</li>
    <li><svg width="10" height="9" viewBox="0 0 10 9"><path d="M1 5 L4 8 L9 1" fill="none" stroke="#4a9a20" stroke-width="2"/></svg>100% E Commerce is feasible</li>
    <li><svg width="10" height="9" viewBox="0 0 10 9"><path d="M1 5 L4 8 L9 1" fill="none" stroke="#4a9a20" stroke-width="2"/></svg>Sheer size of audience necessitates ATL</li>
  </ul>
</div>
<div class="abs shelf" style="left:401px"></div>

<footer class="abs footer"></footer>
<div class="abs f-head" style="left:104px">NAVIGATION</div>
<ul class="abs f-list" style="left:104px;top:1032px">
  <li><span class="bul"></span>Home</li><li><span class="bul"></span>Information</li><li><span class="bul"></span>About Us</li><li><span class="bul"></span>Blog</li><li><span class="bul"></span>Case Study</li><li><span class="bul"></span>Contact</li>
</ul>
<div class="abs f-head" style="left:228px">LATEST BLOG POST</div>
<div class="abs f-blog-t">Marketing to B2B</div>
<div class="abs f-blog">When you are marketing to a B2B you want to focus on the logic of the product. You do this by focusing on the features of the product.</div>
<div class="abs f-head" style="left:394px">FOLLOW US</div>
<ul class="abs f-list" style="left:402px;top:1032px">
  <li><span class="ico"></span>Community</li><li><span class="ico"></span>Updates</li><li><span class="ico"></span>Videos</li><li><span class="ico"></span>Newsletter</li><li><span class="ico"></span>RSS Feed</li>
</ul>
<div class="abs f-head" style="left:540px">CONTACT INFO</div>
<div class="abs" style="left:548px;top:1036px;font-size:8px;line-height:11px;color:var(--footer-text)">
  <svg class="abs" style="left:0;top:0" width="8" height="10" viewBox="0 0 8 10"><path d="M4 10 L1 5 A3.5 3.5 0 1 1 7 5 Z" fill="#c4161c"/></svg>
  <div style="padding-left:20px">Quay Lane 48<br>Norrvik, 4419<br>Sweden</div>
</div>
<ul class="abs f-list" style="left:548px;top:1078px">
  <li><span class="ico" style="background:none;border:1.5px solid #c4161c"></span>+ 555 204 318</li>
  <li><span class="ico"></span>+ 555 204 319</li>
  <li><span class="ico" style="height:6px"></span>info@harbortandem.com</li>
</ul>
<div class="abs copy">©2012 harbortandem.com. All rights reserved.</div>

</body>
</html>
```